Attract customers for New Zealand forest eco tour

Website design for a new eco tourism business in New Zealand. We have domain name booked for it: www.GlenofTakeke.co.nz

We have written the site, see attachments. And have all the pictures to go with it, have just attached a few of these for examples. Will provide the rest to the winning bidder.

We want the look of the site to be highly visually attractive, clean and uncluttered. And if you know about what works best for eco-tourism, that will help.

Website should be mobile phone readable, as well as desktop.

Our objectives for the site are to introduce our forest to them, get people interested in visiting, and have people book trips. We will need some kind of booking app such as with dates of bookings, and ideally a payment app as well so they can pay for bookings.

Ideally, I don't know if you can do this, you use a format which allows us to self edit the site (note, we're not technical experts).

Target Market(s)

Professional people aged 30 - 49.
Looking to travel, probably as a couple.
International travel for adventure, relaxation.

Key things they want are:

See attractions
Go to a place different from their own country
Escape from their usual working life
Unwind and relax

Colors
9bcb3b

Requirements
Must have
• Visually attractive - pictorial look
• Clean and uncluttered - blank space
• Mobile readable and desktop
• Booking app
• Payment app
Nice to have
• Be self editable by us (non-technical people)
Should not have
• shouldn't look cheap

```html
<!DOCTYPE html>
<html lang="en">
<head>
<meta charset="utf-8">
<title>Glen of Takeke</title>
<link href="https://fonts.googleapis.com/css2?family=Open+Sans:wght@400;600;700&display=swap" rel="stylesheet">
<style>
:root{
  --green:#9bcb3b;
  --green-dark:#7fae25;
  --blue:#1d5c96;
  --blue-light:#2f78b8;
  --blue-btn:#2a6db0;
  --ink:#333;
  --muted:#666;
  --dark:#2b2b2b;
  --nav:rgba(30,30,30,.78);
  --field:#fbf8e6;
  --field-line:#cfd89b;
}
*{box-sizing:border-box;margin:0;padding:0}
html,body{width:1200px;height:2880px;overflow:hidden}
body{font-family:"Open Sans",Arial,sans-serif;color:var(--ink);background:#fff;position:relative}
section,header,footer{position:absolute;left:0;width:1200px}

/* header + hero */
.hero{top:0;height:570px;background:linear-gradient(160deg,#5f7d3a 0%,#3d5a2a 35%,#8fa86a 60%,#4b6b33 80%,#2e4421 100%)}
.site-bar{top:0;height:50px;background:var(--nav);display:flex;align-items:center;padding:0 108px;justify-content:space-between;z-index:2}
.brand{color:var(--green);font-weight:700;font-size:28px}
.nav{display:flex;gap:22px;list-style:none}
.nav a{color:#ddd;font-size:14px;text-decoration:none}
.nav a.active{color:var(--green)}

/* welcome */
.welcome{top:570px;height:330px;text-align:center}
.h2{font-size:30px;font-weight:600;color:var(--ink);letter-spacing:.5px}
.welcome .h2{margin-top:38px}
.lead{font-size:14px;color:var(--muted);margin-top:6px}
.tour{position:absolute;top:142px;width:476px;height:160px;border:1px solid #ddd;background:linear-gradient(90deg,#c9d8e4,#eef2f5 40%,#e9eef2);text-align:center;padding-top:22px}
.tour.left{left:112px}.tour.right{left:612px}
.tour h3{font-size:34px;font-weight:400;color:#3d4a55}
.tour p{font-size:14px;color:#444;margin-top:2px}
.btn{display:inline-block;background:var(--blue-btn);color:#fff;font-size:13px;padding:6px 18px;margin-top:14px;text-decoration:none}

/* project */
.project{top:912px;height:272px;background:var(--green);text-align:center;color:#fff}
.project .h2{color:#fff;margin-top:52px}
.project p{font-size:13px;width:720px;margin:14px auto 0;line-height:20px}
.project .btn{margin-top:26px}

/* activities */
.activities{top:1200px;height:520px;text-align:center}
.activities .h2{margin-top:18px}
.activities .lead{color:#444}
.grid{position:absolute;top:112px;left:112px;width:976px;display:grid;grid-template-columns:repeat(4,1fr);row-gap:34px}
.activity{display:flex;flex-direction:column;align-items:center}
.activity .ico{width:124px;height:124px;border-radius:50%;background:radial-gradient(circle at 50% 40%,var(--blue-light),var(--blue) 70%);position:relative}
.activity .ico::after{content:"";position:absolute;inset:14px;border-radius:50%;border:2px solid rgba(255,255,255,.55)}
.activity span{font-size:13px;font-weight:700;margin-top:14px;width:200px;line-height:18px}

/* attractions */
.attractions{top:1728px;height:440px;background:linear-gradient(90deg,#4a4538,#6b6450 30%,#5a5643 60%,#3c3a30);text-align:center;color:#fff}
.attractions .h2{color:#fff;margin-top:26px}
.attractions .lead{color:#eee}
.card{position:absolute;top:136px;width:312px;height:244px}
.card .photo{position:absolute;inset:0}
.c1{left:104px}.c1 .photo{background:linear-gradient(135deg,#7d8a5a,#4c7a86 50%,#8b7a52)}
.c2{left:444px}.c2 .photo{background:linear-gradient(135deg,#9b2a2a,#c84040 40%,#4d6b34)}
.c3{left:776px}.c3 .photo{background:linear-gradient(135deg,#6f7c52,#52808b 50%,#8f805a)}
.price{position:absolute;top:10px;left:10px;background:var(--green);color:#fff;font-size:12px;font-weight:700;padding:3px 8px}
.card .title{position:absolute;left:0;right:0;top:164px;background:rgba(155,203,59,.7);text-align:left;font-size:12px;padding:10px 14px;height:80px}
.days{position:absolute;right:16px;top:150px;width:64px;height:64px;border-radius:50%;background:var(--blue);border:3px solid #fff;font-size:12px;font-weight:700;line-height:15px;padding-top:14px}

/* contact */
.contact{top:2168px;height:392px}
.contact .h2{text-align:center;margin-top:42px}
.label{position:absolute;left:120px;color:var(--green-dark);font-weight:700;font-size:15px}
.info{position:absolute;left:264px;font-size:12px;color:var(--muted);line-height:18px}
.field{position:absolute;background:var(--field);border:1px solid var(--field-line);height:40px}
.field svg{position:absolute;left:10px;top:12px}
.send{position:absolute;left:888px;top:308px;width:176px;height:36px;border:1px solid var(--field-line);color:var(--green-dark);font-size:12px;display:flex;align-items:center;justify-content:center}

/* map + footer */
.map{top:2560px;height:260px}
.map-area{position:absolute;inset:0;background:linear-gradient(160deg,#e8ecde,#dde4d0 40%,#e6e9e0 70%,#d6dccd)}
.map-pin{position:absolute;left:588px;top:92px}
.zoom{position:absolute;right:12px;top:190px;width:26px;background:#fff;border:1px solid #ccc}
.zoom div{height:26px;display:flex;align-items:center;justify-content:center;font-size:18px;color:#555}
.zoom div+div{border-top:1px solid #ddd}
.map-corner{position:absolute;left:12px;bottom:12px;width:30px;height:30px;background:#888}
.footer{top:2820px;height:60px;background:var(--dark);display:flex;align-items:center;justify-content:space-between;padding:0 108px;color:#ccc;font-size:13px}
.social{display:flex;gap:6px}
.social i{width:28px;height:28px;display:block}
</style>
</head>
<body>

<section class="hero" role="img" aria-label="Photograph of a native owl perched among forest branches"></section>
<header class="site-bar">
  <div class="brand">Glen of Takeke</div>
  <ul class="nav">
    <li><a class="active" href="#">Home</a></li>
    <li><a href="#">About Us</a></li>
    <li><a href="#">Tours</a></li>
    <li><a href="#">Project</a></li>
    <li><a href="#">Activities</a></li>
    <li><a href="#">Gallery</a></li>
    <li><a href="#">Contact US</a></li>
  </ul>
</header>

<section class="welcome">
  <h2 class="h2">WELCOME TO OUR SITE</h2>
  <p class="lead">Glen of Takeke is a beautiful native forest in the Far North of New Zealand</p>
  <div class="tour left">
    <h3>OVERNIGHT TOURS</h3>
    <p>Around 1 kilometre into the forest we have a camp set up.</p>
    <a class="btn" href="#">Read more</a>
  </div>
  <div class="tour right">
    <h3>DAY TRIPS TOURS</h3>
    <p>If you'd like to spend a day in the forest let us know when</p>
    <a class="btn" href="#">Read more</a>
  </div>
</section>

<section class="project">
  <h2 class="h2">OUR PROJECT</h2>
  <p>In the far North, our forest is being restored for the native birds and trees that call it home. Your visit supports weed and pest control, so that the forest can thrive for years to come.</p>
  <a class="btn" href="#">Read more</a>
</section>

<section class="activities">
  <h2 class="h2">OUR ACTIVITIES</h2>
  <p class="lead">You can do what you like as activities. These are some of things we enjoy, and visitors to the forest we've had really.</p>
  <div class="grid">
    <div class="activity"><div class="ico" role="img" aria-label="Tree icon"></div><span>GRANDFATHER OF THE FOREST</span></div>
    <div class="activity"><div class="ico" role="img" aria-label="Owl icon"></div><span>BIRDWATCHER</span></div>
    <div class="activity"><div class="ico" role="img" aria-label="Food bowl icon"></div><span>FOREST GOURMET</span></div>
    <div class="activity"><div class="ico" role="img" aria-label="Crayfish icon"></div><span>CRAYFISH HUNTER</span></div>
    <div class="activity"><div class="ico" role="img" aria-label="Forester icon"></div><span>FORESTMAN</span></div>
    <div class="activity"><div class="ico" role="img" aria-label="Orchid icon"></div><span>ORCHID OBSESSIVE</span></div>
    <div class="activity"><div class="ico" role="img" aria-label="Giant tree icon"></div><span>PURIRI GIANT LEGS</span></div>
    <div class="activity"><div class="ico" role="img" aria-label="Tree icon"></div><span>TREE GURU</span></div>
  </div>
</section>

<section class="attractions">
  <h2 class="h2">LOCAL ATTRACTIONS</h2>
  <p class="lead">If you're coming to this part of the country, there are some awesome local attractions to enjoy</p>
  <div class="card c1"><div class="photo" role="img" aria-label="Photograph of a river through native bush"></div><div class="price">$7.00</div><div class="title">Kauri coast river walk</div><div class="days">11<br>DAYS</div></div>
  <div class="card c2"><div class="photo" role="img" aria-label="Photograph of red pohutukawa flowers"></div><div class="price">$7.00</div><div class="title">Coastal flower trail</div><div class="days">11<br>DAYS</div></div>
  <div class="card c3"><div class="photo" role="img" aria-label="Photograph of a river through native bush"></div><div class="price">$7.00</div><div class="title">Kauri coast river walk</div><div class="days">11<br>DAYS</div></div>
</section>

<section class="contact">
  <h2 class="h2">CONTACT US</h2>
  <div class="label" style="top:120px">Our Address</div>
  <div class="info" style="top:120px">12 Forest Road, Far North,<br>New Zealand 0400</div>
  <div class="label" style="top:222px">Phone Number</div>
  <div class="info" style="top:222px">0800 000 000<br>0800 111 111</div>
  <div class="label" style="top:276px">Email Id</div>
  <div class="info" style="top:276px">hello@glenoftakeke.co.nz<br>bookings@glenoftakeke.co.nz</div>

  <div class="field" style="left:448px;top:112px;width:304px">
    <svg width="16" height="16" viewBox="0 0 16 16"><circle cx="8" cy="5" r="3.5" fill="none" stroke="#888" stroke-width="1.4"/><path d="M2 15c0-4 3-6 6-6s6 2 6 6" fill="none" stroke="#888" stroke-width="1.4"/></svg>
  </div>
  <div class="field" style="left:780px;top:112px;width:308px">
    <svg width="18" height="14" viewBox="0 0 18 14"><rect x="1" y="1" width="16" height="12" fill="none" stroke="#888" stroke-width="1.4"/><path d="M1 1l8 7 8-7" fill="none" stroke="#888" stroke-width="1.4"/></svg>
  </div>
  <div class="field" style="left:448px;top:176px;width:640px;height:104px">
    <svg width="16" height="16" viewBox="0 0 16 16"><path d="M2 14l2-5 8-8 3 3-8 8z" fill="none" stroke="#888" stroke-width="1.4"/></svg>
  </div>
  <div class="send">Send a Message</div>
</section>

<section class="map">
  <div class="map-area" role="img" aria-label="Street map showing the forest location"></div>
  <svg class="map-pin" width="24" height="36" viewBox="0 0 24 36" aria-hidden="true"><path d="M12 1C6 1 1 6 1 12c0 8 11 22 11 22s11-14 11-22C23 6 18 1 12 1z" fill="#d9453a" stroke="#9e2d24" stroke-width="1.2"/><circle cx="12" cy="12" r="4" fill="#fff"/></svg>
  <div class="zoom"><div>+</div><div>−</div></div>
  <div class="map-corner"></div>
</section>

<footer class="footer">
  <div>Copyright © 2015 lorem ipsum dolor</div>
  <div class="social">
    <i style="background:#3b5998"></i>
    <i style="background:#29a9e1"></i>
    <i style="background:#d34836"></i>
    <i style="background:#0e76a8"></i>
  </div>
</footer>

</body>
</html>
```